ZRT Pty Ltd business card

we need to get a business card designed. We're a large whole seller of baby formula , health supplement and cosmetic products.

Target Market(s)

Big online E commerce platforms, supermarket channels in Asia.

Industry/Entity Type

Business

Contact Information for Business Card

glossy

Logo Text

ZRT

Colors
abd036

Requirements
Must have
• ZRT

```html
<!DOCTYPE html>
<html lang="en">
<head>
<meta charset="utf-8">
<title>ZRT Pty Ltd – Business Card</title>
<link href="https://fonts.googleapis.com/css2?family=Lato:wght@300;400;700&display=swap" rel="stylesheet">
<style>
  :root {
    --canvas-bg: #2b2b2b;
    --card-white: #f7f7f7;
    --card-dark: #4a4b4c;
    --card-dark-edge: #3a3b3c;
    --accent: #abd036;
    --text-grey: #8a8a8a;
    --text-dark: #6b6b6b;
    --divider: #c9c9c9;
  }
  * { margin: 0; padding: 0; box-sizing: border-box; }
  html, body {
    width: 1200px; height: 900px; overflow: hidden;
    background: var(--canvas-bg);
    font-family: "Lato", sans-serif;
  }
  .canvas {
    position: relative; width: 1200px; height: 900px;
    display: flex; flex-direction: column; align-items: center; justify-content: center; gap: 50px;
  }
  .card {
    width: 560px; height: 320px;
    box-shadow: 0 12px 30px rgba(0,0,0,.45);
    position: relative;
  }
  .card--front {
    background: var(--card-white);
    display: flex; align-items: center;
    padding: 0 40px 0 48px;
  }
  .identity { width: 190px; text-align: right; padding-right: 28px; }
  .identity__name {
    color: var(--accent); font-weight: 700; font-size: 19px; letter-spacing: .3px;
    text-transform: uppercase;
  }
  .identity__role { color: var(--text-dark); font-weight: 400; font-size: 14px; margin-top: 2px; }
  .divider { width: 1px; height: 70px; background: var(--divider); }
  .contact { padding-left: 28px; color: var(--text-grey); font-size: 13px; font-weight: 400; line-height: 1.75; }
  .contact__row { display: flex; align-items: center; gap: 6px; white-space: nowrap; }
  .contact__row + .contact__row { margin-top: 0; }
  .contact__group { display: flex; gap: 16px; }
  .contact__icon { width: 11px; height: 11px; flex: none; }
  .contact strong { font-weight: 700; color: var(--text-dark); }
  .card--back {
    background: radial-gradient(ellipse at 50% 35%, #5a5b5c 0%, var(--card-dark) 55%, var(--card-dark-edge) 100%);
    display: flex; align-items: center; justify-content: center; gap: 14px;
  }
  .brand__dot { width: 16px; height: 16px; border-radius: 50%; background: var(--accent); }
  .brand__name {
    color: var(--accent); font-weight: 700; font-size: 64px; letter-spacing: 4px; line-height: 1;
  }
</style>
</head>
<body>
<main class="canvas">
  <section class="card card--front" aria-label="Card front">
    <div class="identity">
      <p class="identity__name">Daniel Moreau</p>
      <p class="identity__role">Managing Director</p>
    </div>
    <div class="divider"></div>
    <div class="contact">
      <p class="contact__row">A-0000 Lindenport, Place du Marché 00</p>
      <div class="contact__group">
        <p class="contact__row">
          <svg class="contact__icon" viewBox="0 0 12 12"><path fill="#abd036" d="M2.5 1h2l1 2.5-1.3 1a6 6 0 0 0 3.3 3.3l1-1.3L11 7.5v2a1.5 1.5 0 0 1-1.5 1.5A8.5 8.5 0 0 1 1 2.5 1.5 1.5 0 0 1 2.5 1z"/></svg>
          000-000-0000
        </p>
        <p class="contact__row">
          <svg class="contact__icon" viewBox="0 0 12 12"><rect x="1" y="2.5" width="10" height="7" rx="1" fill="#abd036"/><path d="M1.5 3l4.5 3.5L10.5 3" fill="none" stroke="#f7f7f7" stroke-width="1"/></svg>
          daniel@<strong>zrt</strong>.com
        </p>
      </div>
      <p class="contact__row">
        <svg class="contact__icon" viewBox="0 0 12 12"><circle cx="6" cy="6" r="5" fill="none" stroke="#abd036" stroke-width="1.4"/><path d="M1 6h10M6 1c2 2 2 8 0 10M6 1c-2 2-2 8 0 10" fill="none" stroke="#abd036" stroke-width="1"/></svg>
        www.<strong>zrt</strong>.com
      </p>
    </div>
  </section>

  <section class="card card--back" aria-label="Card back">
    <span class="brand__dot"></span>
    <span class="brand__name">ZRT</span>
  </section>
</main>
</body>
</html>
```